Client Welcome Pack Brochure Design

Hi, we need a two page A4 document designed. We are a financial services company, providing financial planning, share trading, mortgage broking and many other services.
We need a 'Client Welcome Pack' for new clients to receive before their first meeting.
Content and style guide provided - use these to design a document.
One page - A4 - front and back.
No need to write anything or fill with placeholder text - DESIGN ONLY

```html
<!DOCTYPE html>
<html lang="en">
<head>
<meta charset="utf-8">
<title>Client Welcome Pack</title>
<link href="https://fonts.googleapis.com/css2?family=Montserrat:wght@700;800&family=Open+Sans:wght@400;600;700&family=Oswald:wght@400&display=swap" rel="stylesheet">
<style>
:root{
  --navy:#22398a;
  --blue:#1d5ea8;
  --blue-deep:#1a4f94;
  --yellow:#f6b71d;
  --paper:#ececef;
  --grey:#d9d9dd;
  --ink:#3a3a3f;
  --body:#555559;
  --backdrop:#e4e4e8;
}
*{box-sizing:border-box;margin:0;padding:0}
html,body{width:1200px;height:2764px;overflow:hidden;background:var(--backdrop)}
body{position:relative;font-family:"Open Sans",Arial,sans-serif;color:var(--body)}
.page{position:absolute;left:228px;width:772px;height:1045px;background:var(--paper);overflow:hidden;box-shadow:0 18px 30px rgba(0,0,0,.22)}
.page--front{top:168px}
.page--back{top:1548px}
.abs{position:absolute}

/* front */
.header-panel{left:0;top:0;width:386px;height:499px;background:var(--grey);clip-path:polygon(0 0,100% 0,100% 100%,0 415px)}
.hero-photo{left:385px;top:0;width:387px;height:499px;background:linear-gradient(160deg,#7fa3cf 0%,#5b86bd 45%,#3f6ea8 100%);clip-path:polygon(0 0,100% 0,100% 415px,0 100%)}
.brand{display:flex;align-items:center;gap:6px;font-family:"Open Sans",sans-serif;font-weight:700;color:var(--navy);font-size:11px;line-height:1.2;text-transform:uppercase;letter-spacing:.5px}
.brand--primary{left:40px;top:48px;width:95px;flex-direction:column;text-align:center}
.brand--primary .mark{width:44px;height:44px;border-radius:50%;background:var(--navy)}
.brand--partner{left:228px;top:72px;font-size:15px;text-transform:none;letter-spacing:0;flex-direction:column}
.brand--partner .mark{width:30px;height:30px;background:var(--navy)}
.brand-divider{left:175px;top:44px;width:1px;height:90px;background:#b9b9c0}
.pack-title{left:37px;top:172px;font-family:"Montserrat",sans-serif;font-weight:800;font-size:37px;line-height:40px;color:var(--navy);letter-spacing:.5px}
.pack-tag{left:37px;top:303px;height:43px;padding:0 9px;background:var(--yellow);font-family:"Oswald",sans-serif;font-size:27px;line-height:43px;color:#222}
.pack-licence{left:37px;top:361px;font-weight:700;font-size:14.5px;line-height:18px;color:#222}
.welcome{left:53px;top:540px;width:680px}
.section-head{font-family:"Montserrat",sans-serif;font-weight:800;font-size:17px;color:var(--blue);letter-spacing:.3px}
.welcome p{font-size:14.5px;line-height:18.5px;color:var(--body);margin-top:8px}
.welcome p + p{margin-top:7px}
.meeting-band{left:0;top:669px;width:772px;height:337px;background:linear-gradient(180deg,#3a79bf 0%,#2a66ad 55%,#2260a7 100%);clip-path:polygon(0 0,50% 86px,100% 0,100% 100%,0 100%)}
.bottom-stripe{left:0;top:1006px;width:772px;height:39px;background:var(--yellow)}
.meeting{left:53px;top:840px;width:680px;color:#fff}
.meeting h2{font-family:"Montserrat",sans-serif;font-weight:800;font-size:17px;color:var(--yellow)}
.meeting p{font-size:14.5px;line-height:18px;margin-top:8px}

/* back */
.services-photo{left:395px;top:0;width:377px;height:460px;background:linear-gradient(155deg,#a9c3e3 0%,#7fa3cf 50%,#5b86bd 100%);clip-path:polygon(0 0,100% 0,100% 400px,0 100%)}
.solutions{left:467px;top:316px;width:238px;height:298px;background:var(--yellow);clip-path:polygon(0 0,100% 0,100% 229px,0 100%);padding:26px 22px 0 25px}
.solutions h3{font-family:"Montserrat",sans-serif;font-weight:800;font-size:16.5px;color:var(--blue);letter-spacing:.2px}
.solutions p{font-size:14.5px;line-height:18px;color:#222;text-align:justify;margin-top:4px;margin-bottom:14px}
.services-title{left:40px;top:34px;font-family:"Montserrat",sans-serif;font-weight:800;font-size:30px;line-height:33px;color:var(--blue)}
.timeline{left:55px;top:136px;width:2px;height:570px;background:var(--navy)}
.service{position:absolute;left:84px;width:288px}
.service::before{content:"";position:absolute;left:-39px;top:1px;width:21px;height:21px;border-radius:50%;background:#1f4a74}
.service h4{font-weight:700;font-size:14.5px;color:#2b2b30;line-height:18px}
.service ul{list-style:none;margin-top:1px}
.service li{position:relative;padding-left:18px;font-size:12.5px;line-height:15.6px;color:var(--body);text-align:justify}
.service li::before{content:"";position:absolute;left:1px;top:5px;width:6px;height:6px;border:1px solid #555;border-radius:50%}
.aml{left:84px;top:631px;width:288px;font-size:12.5px;line-height:15.6px;color:var(--body);text-align:justify}
.contact-panel{left:0;top:759px;width:772px;height:286px;background:var(--grey);clip-path:polygon(0 0,100% 120px,100% 100%,0 100%)}
.contacts{left:56px;top:811px}
.contacts p{font-size:14px;line-height:18px;color:var(--body);margin-top:3px}
.office{top:890px;font-size:13.5px;line-height:17.9px;color:var(--body)}
.office h5{font-weight:700;font-size:13.5px;color:#333}
.office--east{left:56px}
.office--south{left:352px}
.office-divider{left:301px;top:890px;width:1px;height:122px;background:#a9a9b0}
</style>
</head>
<body>

<section class="page page--front">
  <div class="abs header-panel"></div>
  <div class="abs hero-photo" role="img" aria-label="Photo of business people shaking hands, blue toned"></div>

  <div class="abs brand brand--primary"><span class="mark"></span><span>Northwind Wealth Partners</span></div>
  <div class="abs brand-divider"></div>
  <div class="abs brand brand--partner"><span class="mark"></span><span>the Keystone Group</span></div>

  <h1 class="abs pack-title">CLIENT<br>WELCOME<br>PACK</h1>
  <div class="abs pack-tag">Essential reading for new clients</div>
  <p class="abs pack-licence">All financial services for new clients under<br>NWP Licensing Ltd. AFSL No. 512093</p>

  <div class="abs welcome">
    <h2 class="section-head">WELCOME</h2>
    <p>Thank you for the opportunity to present our services to you.</p>
    <p>Everything you need to know about Northwind Wealth Partners can be found in our Financial Services Guide (FSG) enclosed and on our website www.northwindwealth.com.au. Our FSG details who we are, our services and service options along with our fees and adviser information.</p>
  </div>

  <div class="abs meeting-band" role="img" aria-label="Photo of a desk with calculator and paperwork, blue toned"></div>
  <div class="abs meeting">
    <h2>Preparing for your first meeting – What to bring</h2>
    <p>If you feel comfortable in doing so, bringing along the following documents will be a great help. Forming an accurate picture of your financial situation helps us in tailoring a financial plan to meet your needs. We're not shy of being flooded with paperwork and information, so if in doubt, bring it along anyway.</p>
  </div>
  <div class="abs bottom-stripe"></div>
</section>

<section class="page page--back">
  <div class="abs services-photo" role="img" aria-label="Photo of hands reviewing charts and documents at a desk, blue toned"></div>
  <div class="abs solutions">
    <h3>CUSTOM SOLUTIONS</h3>
    <p>We can customise a financial or investment plan to suit your personal needs.</p>
    <h3>ONLINE SOLUTIONS</h3>
    <p>You will be able to access all of your information online via our secure online client portal.</p>
  </div>

  <h2 class="abs services-title">Our<br>Services</h2>
  <div class="abs timeline"></div>

  <div class="service" style="top:126px">
    <h4>Income Sources</h4>
    <ul>
      <li>Salary/employment (latest pay slip, PAYG summary and accounting records)</li>
      <li>Centrelink benefits information</li>
      <li>Rental Income</li>
      <li>Pension or annuity details</li>
      <li>Tax returns</li>
    </ul>
  </div>
  <div class="service" style="top:255px">
    <h4>Assets &amp; Income details</h4>
    <ul>
      <li>Superannuation funds</li>
      <li>Shares (contract notes, dividend details, reinvestment plans)</li>
      <li>Bank accounts, term deposits, managed funds</li>
      <li>Investment properties (cost details)</li>
    </ul>
  </div>
  <div class="service" style="top:387px">
    <h4>Liabilities / sources of debt</h4>
    <ul>
      <li>Home loan</li>
      <li>Credit cards</li>
      <li>Personal and car loans</li>
      <li>Investment loans</li>
    </ul>
  </div>
  <div class="service" style="top:484px">
    <h4>Miscellaneous information</h4>
    <ul>
      <li>Any insurance details</li>
      <li>Tax file number</li>
      <li>Accountant contact information</li>
      <li>Annual accounts for related entities (SMSF, companies, trusts or partnerships)</li>
      <li>Driver's license, birth certificate, passport, Medicare card for identification</li>
    </ul>
  </div>
  <p class="abs aml">As part of our obligations under the Anti-Money Laundering and Counter Terrorism Financing Rules we are required to verify your full name and either date of birth or residential address. An acceptable document for this is a driver's license or passport.</p>

  <div class="abs contact-panel"></div>
  <div class="abs contacts">
    <h2 class="section-head">CONTACTS</h2>
    <p>You can contact all staff directly either<br>via email or phone.</p>
  </div>
  <div class="abs office office--east">
    <h5>Eastport Office</h5>
    58 Harbour Street<br>EASTPORT QLD<br>PO Box 218<br>1800 555 210<br>enquiries@northwindwealth.com.au<br>www.northwindwealth.com.au
  </div>
  <div class="abs office-divider"></div>
  <div class="abs office office--south">
    <h5>Southbank Office</h5>
    Level 2, 17 Carrington Road<br>ASHFIELD VIC<br>PO Box 906<br>1800 555 347<br>clientinfo@keystonegroup.com.au<br>www.northwindwealth.com.au
  </div>
</section>

</body>
</html>
```